Opening a Hair Salon

Looking for a design for my sign that looks high end, an emphasis on color but welcoming to men and women.

The name is Norvale Haircuts and Colors

Trying capture a more affluent client. Looking for a very modern look.

Reason: Time is going to quick and would like to see a few more options.

Hair

```html
<!DOCTYPE html>
<html lang="en">
<head>
<meta charset="utf-8">
<title>Norvale Haircuts and Colors – Sign</title>
<link rel="stylesheet" href="https://fonts.googleapis.com/css2?family=Antonio:wght@200;300&family=Share+Tech+Mono&display=swap">
<style>
  :root {
    --sign-black: #000000;
    --sign-white: #ffffff;
    --ornament-tone: rgba(255, 255, 255, 0.55);
  }
  html, body {
    margin: 0;
    padding: 0;
    overflow: hidden;
    background: var(--sign-black);
  }
  .sign {
    position: relative;
    width: 1200px;
    height: 360px;
    background: var(--sign-black);
    color: var(--sign-white);
    overflow: hidden;
  }
  .sign__name {
    position: absolute;
    top: 22px;
    left: 0;
    width: 100%;
    margin: 0;
    text-align: center;
    font-family: "Antonio", "Arial Narrow", sans-serif;
    font-weight: 300;
    font-size: 136px;
    line-height: 1;
    letter-spacing: 4px;
    text-transform: uppercase;
  }
  .sign__services {
    position: absolute;
    top: 194px;
    left: 0;
    width: 100%;
    margin: 0;
    text-align: center;
    font-family: "Share Tech Mono", monospace;
    font-weight: 400;
    font-size: 38px;
    line-height: 1;
    letter-spacing: 6px;
    text-transform: uppercase;
  }
  .sign__ornament {
    position: absolute;
    top: 256px;
    left: 462px;
    width: 276px;
    height: 30px;
    border-radius: 50%;
    background: radial-gradient(ellipse at center, var(--ornament-tone) 0%, rgba(255,255,255,0.15) 55%, rgba(255,255,255,0) 75%);
  }
  .sign__phone {
    position: absolute;
    top: 308px;
    left: 0;
    width: 100%;
    margin: 0;
    text-align: center;
    font-family: "Share Tech Mono", monospace;
    font-size: 24px;
    line-height: 1;
    letter-spacing: 3px;
  }
</style>
</head>
<body>
  <main class="sign">
    <h1 class="sign__name">Norvale</h1>
    <p class="sign__services">Haircuts and Colors</p>
    <div class="sign__ornament" role="img" aria-label="Decorative white scroll flourish divider"></div>
    <p class="sign__phone">555-010-246</p>
  </main>
</body>
</html>
```